Tapfold Nest mobile app; beer delivery service

We are looking for a design of our app - "Tapfold Nest". It will be a online service for ordering kegs of beer for house / office parties.

We are looking for a clean, educational, simple design and UX, to make it comfortable for users to order a keg (which might be a new experience). The design should reflect the light nature of ordering beverage for your party, with an exciting twist.

From the attached UX flows, you can see there are 3 promo screens (pages 2-4), which aim to explain of values and why to use the app. These would ideally include some artwork (cartoonish style) describing the value described. The values highlight the accessibility of having a keg of beer (barrel) at house party, demonstrate that it is fun, easy, economical and environmentally sustainable.

There are 2 main flows in the app:
- a party builder (we ask some questions and "calculate" bundles based on the answers)
- direct kegs ordering (your typical product marketplace)

Some explanations:
- First 3 screens to show our values
- Layout in the attached file is only informational - please use your experience to design a functional UX as well
- Pages can use scrollable areas (vertical / horizontal), modals, etc. We will use FluxFrame so you can use those components in your design.
- Animation screen, when the party is being calculated (would be nice)
- The payment Screen will use the default Paxel payment sheet component (incl. Orchid / Zentry pay or credit card info)
- There is no logo yet, you can use just simple text on the splash screen
- There is no log-in functionality, so don't bother including login/signup screen or a profile area in the app
- for images of beers / breweries, you can use logo of https://www.harlowmeadales.example/ or similar (not actually images of beers)
- some of the offered beers / breweries / bundles might be Featured or otherwise prioritised, so it should be shown in the design

Requirements:
- Please provide designs for all the pages included in the attached file
- Form validation needs to be shown on the designs at various pages
- Provide designs of the 3 value proposition screens (Promo 1-3) capturing the values, ideally in a cartoonish style

Target Market(s)

Households

Industry/Entity Type

Food and beverage, delivery

Font styles to use
Sans Serif

Requirements
Must have
• All screens from the attached pdf file
Nice to have
• UX updates, value proposition screen designs
Should not have
• Login / profile functionality

```html
<!DOCTYPE html>
<html lang="en">
<head>
<meta charset="utf-8">
<title>Tapfold Nest – App Screens</title>
<link href="https://fonts.googleapis.com/css2?family=Montserrat:ital,wght@0,900;1,500;1,900&family=Source+Sans+3:wght@400;600&display=swap" rel="stylesheet">
<style>
  :root{
    --stage:#4d4d4d;
    --cream:#fde8d3;
    --orange:#fbab48;
    --pink:#f77b7b;
    --ink:#2b2b2b;
    --white:#ffffff;
    --line:#3a3a3a;
  }
  *{box-sizing:border-box;margin:0;padding:0}
  html,body{width:1056px;height:1200px;overflow:hidden;background:var(--stage)}
  body{position:relative;font-family:"Source Sans 3",sans-serif;color:var(--ink)}
  .screen{position:absolute;width:234px;overflow:hidden}
  .screen--cream{background:var(--cream)}
  .screen--white{background:var(--white)}
  .status{position:absolute;top:6px;left:13px;right:13px;height:12px;display:flex;justify-content:space-between;align-items:center;font-size:8px;font-weight:600}
  .status svg{display:block}
  .band{position:absolute;left:0;top:0;width:234px;height:217px;background:var(--orange);border-radius:0 0 18px 18px}
  .art{position:absolute;left:37px;top:52px;width:160px;height:190px;border-radius:14px;background:linear-gradient(170deg,#f3f3f3 0%,#d6d6d6 45%,#2a2a2a 100%);opacity:.85}
  .skip{position:absolute;top:37px;right:17px;font-size:7.5px;font-weight:600}
  .back{position:absolute;top:35px;left:15px}
  .heading{position:absolute;left:13px;font-family:"Montserrat",sans-serif;font-weight:900;font-style:italic;font-size:20px;line-height:24px;letter-spacing:-.2px;color:var(--ink)}
  .body{position:absolute;left:13px;width:210px;font-size:9.6px;line-height:15.9px}
  .hl{color:var(--orange);font-weight:600}
  .dots{position:absolute;top:462px;left:13px;display:flex;gap:4px;align-items:center}
  .dot{width:4px;height:4px;border-radius:50%;background:var(--orange)}
  .dash{width:23px;height:4px;border-radius:2px;background:var(--orange)}
  .next{position:absolute;left:119px;top:450px;width:102px;height:28px;border-radius:14px;background:var(--orange);color:var(--white);font-size:9px;display:flex;align-items:center;justify-content:center;gap:14px;box-shadow:0 2px 3px rgba(0,0,0,.12)}
  .label{position:absolute;left:13px;font-size:9.3px;line-height:12px}
  .field{position:absolute;left:13px;width:207px;height:29px;border:1px solid var(--line);border-radius:8px;font-size:6.8px;color:#555;display:flex;align-items:center;justify-content:space-between;padding:0 9px}
  .hint{position:absolute;left:19px;font-size:6.6px;font-weight:600;color:var(--orange);line-height:9px}
  .cta{position:absolute;left:13px;width:208px;height:35px;border-radius:18px;background:var(--orange);color:var(--white);font-size:10.5px;font-weight:600;display:flex;align-items:center;justify-content:center;box-shadow:0 2px 3px rgba(0,0,0,.12)}
  .mugs{position:absolute;border-radius:10px;background:radial-gradient(circle at 50% 55%,#fbab48 0%,#fcd9a8 60%,#ffffff 100%)}
  .card{position:absolute;left:13px;width:207px;border:1px solid var(--line);border-radius:8px}
  .question{position:absolute;left:14px;width:172px;font-family:"Montserrat",sans-serif;font-style:italic;font-weight:500;font-size:11.3px;line-height:13px}
  .pill{position:absolute;width:136px;height:35px;border-radius:18px;color:var(--white);font-size:10.5px;font-weight:600;display:flex;align-items:center;justify-content:center;box-shadow:0 2px 3px rgba(0,0,0,.12)}
  .pill--pink{background:var(--pink)}
  .pill--orange{background:var(--orange)}
  .sub{position:absolute;left:13px;font-family:"Montserrat",sans-serif;font-style:italic;font-weight:500;font-size:11px;line-height:13px}
  .slider{position:absolute;left:13px;width:203px;height:1px;background:var(--line)}
  .knob{position:absolute;top:-10px;width:20px;height:20px;border-radius:50%;background:var(--orange);border:1px solid var(--line);font-size:8px;display:flex;align-items:center;justify-content:center}
  .splash-mark{position:absolute;left:63px;top:145px;width:108px;height:108px;border-radius:50%;background:var(--orange);border:11px solid var(--ink)}
  .brand{position:absolute;left:0;width:234px;text-align:center;top:261px;font-family:"Montserrat",sans-serif;font-weight:900;font-style:italic;font-size:18px;color:var(--ink)}
</style>
</head>
<body>

<section class="screen screen--cream" style="left:35px;top:34px;height:506px">
  <div class="status"><span>9:41</span><svg width="38" height="8" viewBox="0 0 38 8"><rect x="0" y="5" width="2" height="3"/><rect x="3" y="3.5" width="2" height="4.5"/><rect x="6" y="2" width="2" height="6"/><rect x="9" y="0.5" width="2" height="7.5"/><path d="M15 3a6 6 0 0 1 8 0l-1 1a4.5 4.5 0 0 0-6 0zM17 5a3 3 0 0 1 4 0l-2 2z"/><rect x="26" y="1" width="11" height="6" rx="1.5"/></svg></div>
  <div class="splash-mark"></div>
  <div class="brand">Tapfold Nest</div>
</section>

<section class="screen screen--cream" style="left:286px;top:34px;height:506px">
  <div class="band"></div>
  <div class="art" role="img" aria-label="Cartoon illustration of a host dancing with shopping bags"></div>
  <div class="status"><span>9:41</span><svg width="38" height="8" viewBox="0 0 38 8"><rect x="0" y="5" width="2" height="3"/><rect x="3" y="3.5" width="2" height="4.5"/><rect x="6" y="2" width="2" height="6"/><rect x="9" y="0.5" width="2" height="7.5"/><path d="M15 3a6 6 0 0 1 8 0l-1 1a4.5 4.5 0 0 0-6 0zM17 5a3 3 0 0 1 4 0l-2 2z"/><rect x="26" y="1" width="11" height="6" rx="1.5"/></svg></div>
  <div class="skip">Skip</div>
  <h1 class="heading" style="top:259px">Throw a Bash!</h1>
  <p class="body" style="top:292px">Who loves a party? We all love a party, but we don't all love having to plan for one. Are you over the anxiety that comes with being the hostess with the mostess? Want to make sure your guests are sufficiently fed and watered? Well when it comes to beer drinkers, we got you covered!</p>
  <div class="dots"><span class="dash"></span><span class="dot"></span><span class="dot"></span></div>
  <div class="next">Next <svg width="22" height="8" viewBox="0 0 22 8"><path d="M0 4h20M16 1l4 3-4 3" stroke="#fff" fill="none"/></svg></div>
</section>

<section class="screen screen--cream" style="left:537px;top:34px;height:506px">
  <div class="band"></div>
  <div class="art" role="img" aria-label="Cartoon illustration of a person striding past a large beer hose"></div>
  <div class="status"><span>9:41</span><svg width="38" height="8" viewBox="0 0 38 8"><rect x="0" y="5" width="2" height="3"/><rect x="3" y="3.5" width="2" height="4.5"/><rect x="6" y="2" width="2" height="6"/><rect x="9" y="0.5" width="2" height="7.5"/><path d="M15 3a6 6 0 0 1 8 0l-1 1a4.5 4.5 0 0 0-6 0zM17 5a3 3 0 0 1 4 0l-2 2z"/><rect x="26" y="1" width="11" height="6" rx="1.5"/></svg></div>
  <svg class="back" width="8" height="10" viewBox="0 0 8 10"><path d="M6 1L2 5l4 4" stroke="#2b2b2b" stroke-width="1.3" fill="none"/></svg>
  <div class="skip">Skip</div>
  <h1 class="heading" style="top:259px">More party, less<br>planning!</h1>
  <p class="body" style="top:318px">No more last minute runs to the bottle shop, supermarket or local wholesalers. No more back breaking journeys carrying heavy beer bottles and cans across your neighbourhood. No more worries about fridge capacity and no more warm beers for your guests.</p>
  <div class="dots"><span class="dot"></span><span class="dash"></span><span class="dot"></span></div>
  <div class="next">Next <svg width="22" height="8" viewBox="0 0 22 8"><path d="M0 4h20M16 1l4 3-4 3" stroke="#fff" fill="none"/></svg></div>
</section>

<section class="screen screen--cream" style="left:788px;top:34px;height:506px">
  <div class="band"></div>
  <div class="art" role="img" aria-label="Cartoon illustration of a person carrying a potted plant beside a dollar sign"></div>
  <div class="status"><span>9:41</span><svg width="38" height="8" viewBox="0 0 38 8"><rect x="0" y="5" width="2" height="3"/><rect x="3" y="3.5" width="2" height="4.5"/><rect x="6" y="2" width="2" height="6"/><rect x="9" y="0.5" width="2" height="7.5"/><path d="M15 3a6 6 0 0 1 8 0l-1 1a4.5 4.5 0 0 0-6 0zM17 5a3 3 0 0 1 4 0l-2 2z"/><rect x="26" y="1" width="11" height="6" rx="1.5"/></svg></div>
  <svg class="back" width="8" height="10" viewBox="0 0 8 10"><path d="M6 1L2 5l4 4" stroke="#2b2b2b" stroke-width="1.3" fill="none"/></svg>
  <div class="skip">Skip</div>
  <h1 class="heading" style="top:259px">Save money and<br>the planet!</h1>
  <p class="body" style="top:318px">Finally a <span class="hl">cost efficient, environmentally sustainable, no hassle</span> and <span class="hl">fun</span> way to keep all the beer drinkers at your party smiling. Our service enables you to throw a keg party of your dreams by removing the logistical challenges so you and your guests can focus on having a good time. Never worry about your beer supply again.</p>
  <div class="dots"><span class="dot"></span><span class="dot"></span><span class="dash"></span></div>
  <div class="next">Next <svg width="22" height="8" viewBox="0 0 22 8"><path d="M0 4h20M16 1l4 3-4 3" stroke="#fff" fill="none"/></svg></div>
</section>

<section class="screen screen--white" style="left:35px;top:567px;height:505px">
  <div class="status"><span>9:41</span><svg width="38" height="8" viewBox="0 0 38 8"><rect x="0" y="5" width="2" height="3"/><rect x="3" y="3.5" width="2" height="4.5"/><rect x="6" y="2" width="2" height="6"/><rect x="9" y="0.5" width="2" height="7.5"/><path d="M15 3a6 6 0 0 1 8 0l-1 1a4.5 4.5 0 0 0-6 0zM17 5a3 3 0 0 1 4 0l-2 2z"/><rect x="26" y="1" width="11" height="6" rx="1.5"/></svg></div>
  <svg class="back" width="8" height="10" viewBox="0 0 8 10"><path d="M6 1L2 5l4 4" stroke="#2b2b2b" stroke-width="1.3" fill="none"/></svg>
  <h1 class="heading" style="top:64px">Before we<br>begin..</h1>
  <div class="mugs" role="img" aria-label="Illustration of two clinking beer mugs" style="left:172px;top:63px;width:48px;height:46px"></div>
  <p class="label" style="top:135px">We need to check if we deliver in your area</p>
  <div class="field" style="top:158px">Address Lookup</div>
  <p class="hint" style="top:191px">We only deliver in selected London boroughs during the pilot.</p>
  <p class="label" style="top:225px">Making sure you are grown up</p>
  <div class="field" style="top:248px">Enter date of birth (dd/mm/yyyy)</div>
  <p class="hint" style="top:281px">You have to be 18 years old to use this service.</p>
  <div class="cta" style="top:443px">Let the Party Begin!</div>
</section>

<section class="screen screen--white" style="left:286px;top:567px;height:505px">
  <div class="status"><span>9:41</span><svg width="38" height="8" viewBox="0 0 38 8"><rect x="0" y="5" width="2" height="3"/><rect x="3" y="3.5" width="2" height="4.5"/><rect x="6" y="2" width="2" height="6"/><rect x="9" y="0.5" width="2" height="7.5"/><path d="M15 3a6 6 0 0 1 8 0l-1 1a4.5 4.5 0 0 0-6 0zM17 5a3 3 0 0 1 4 0l-2 2z"/><rect x="26" y="1" width="11" height="6" rx="1.5"/></svg></div>
  <h1 class="heading" style="top:31px">Let’s start ...</h1>
  <div class="mugs" role="img" aria-label="Illustration of two clinking beer mugs" style="left:93px;top:97px;width:47px;height:47px"></div>
  <div class="card" style="top:190px;height:137px">
    <p class="question" style="top:17px">Are you planning a party and want to have some keg fun, but not quite sure what to order?</p>
    <div class="pill pill--pink" style="left:63px;top:86px">Help me plan my party</div>
  </div>
  <div class="card" style="top:341px;height:137px">
    <p class="question" style="top:20px;width:180px">Do you know exactly what you want and want to pick some delicious beer for your party?</p>
    <div class="pill pill--orange" style="left:63px;top:86px">Right to kegs</div>
  </div>
</section>

<section class="screen screen--white" style="left:537px;top:567px;height:598px">
  <div class="status"><span>9:41</span><svg width="38" height="8" viewBox="0 0 38 8"><rect x="0" y="5" width="2" height="3"/><rect x="3" y="3.5" width="2" height="4.5"/><rect x="6" y="2" width="2" height="6"/><rect x="9" y="0.5" width="2" height="7.5"/><path d="M15 3a6 6 0 0 1 8 0l-1 1a4.5 4.5 0 0 0-6 0zM17 5a3 3 0 0 1 4 0l-2 2z"/><rect x="26" y="1" width="11" height="6" rx="1.5"/></svg></div>
  <svg class="back" width="8" height="10" viewBox="0 0 8 10"><path d="M6 1L2 5l4 4" stroke="#2b2b2b" stroke-width="1.3" fill="none"/></svg>
  <h1 class="heading" style="top:31px;left:36px">Tell us about<br>your party ...</h1>
  <h2 class="sub" style="top:103px">When is your party?</h2>
  <div class="field" style="top:128px">Pick a date <svg width="7" height="7" viewBox="0 0 7 7"><rect x="0.5" y="1" width="6" height="5.5" fill="none" stroke="#333" stroke-width=".8"/><path d="M0.5 2.8h6" stroke="#333" stroke-width=".8"/></svg></div>
  <p class="hint" style="top:164px;left:13px;display:flex;align-items:center;gap:4px"><svg width="8" height="8" viewBox="0 0 8 8"><circle cx="4" cy="4" r="3.4" fill="none" stroke="#fbab48" stroke-width=".8"/><path d="M2.4 4.6a1.8 1.8 0 0 0 3.2 0" fill="none" stroke="#fbab48" stroke-width=".8"/></svg>We will pick up the empty keg the next day</p>
  <h2 class="sub" style="top:190px">Tell us about the people attending</h2>
  <p class="label" style="top:218px">Booze hound (good for 8 pints)</p>
  <div class="slider" style="top:248px"><span class="knob" style="left:55px">8</span></div>
  <p class="label" style="top:265px">Thirsty but thoughtful (good for 5 pints)</p>
  <div class="slider" style="top:294px"><span class="knob" style="left:12px">3</span></div>
  <p class="label" style="top:311px">Country club bore (good for 2 pints)</p>
  <div class="slider" style="top:341px"><span class="knob" style="left:44px">7</span></div>
  <h2 class="sub" style="top:370px">What kind of beer do you like?</h2>
  <div class="field" style="top:395px">Beer Selector <svg width="8" height="5" viewBox="0 0 8 5"><path d="M1 1l3 3 3-3" stroke="#333" fill="none" stroke-width=".8"/></svg></div>
  <h2 class="sub" style="top:437px">What kind of glassware do you<br>require?</h2>
  <div class="field" style="top:473px">Glass Selector <svg width="8" height="5" viewBox="0 0 8 5"><path d="M1 1l3 3 3-3" stroke="#333" fill="none" stroke-width=".8"/></svg></div>
  <div class="cta" style="top:531px">Show me the recommendation</div>
</section>

</body>
</html>
```